Ridgeway Hearth Partners Business Card

Looking for a new business card layout. We are a real estate firm w/ a logo, old design attached. Must keep the same elements on there, just need a fresh look and possible some foil accents. Looking for a simpler design w/ more modern style.

Target Market(s)

Real Estate clients

Industry/Entity Type

Real Estate Agent

Contact Information for Business Card

Font styles to use
Sans Serif

Requirements
Must have
• all elements on current biz card
Nice to have
• modern look, simpler than we have!
Should not have
• no serif fonts

```html
<!DOCTYPE html>
<html lang="en">
<head>
<meta charset="utf-8">
<title>Ridgeway Hearth Partners Business Card</title>
<link rel="stylesheet" href="https://fonts.googleapis.com/css2?family=Lato:wght@400;700;900&display=swap">
<style>
  :root {
    --backdrop: #e6e7ea;
    --card: #ffffff;
    --ink: #1d1d1f;
    --ink-soft: #3a3a3e;
    --blue-deep: #3a6cc2;
    --blue-light: #74b6e6;
    --ring: #3f86d3;
    --photo-warm: #d9c6a5;
    --photo-cool: #b8c6cf;
  }
  * { box-sizing: border-box; margin: 0; padding: 0; }
  html, body { width: 1200px; height: 814px; overflow: hidden; }
  body {
    background: var(--backdrop);
    font-family: "Lato", sans-serif;
    color: var(--ink);
    position: relative;
  }
  .card {
    position: absolute;
    width: 500px;
    height: 286px;
    background: var(--card);
    border-radius: 16px;
    overflow: hidden;
    box-shadow: 0 10px 28px rgba(0,0,0,0.18);
  }
  .card--front { left: 70px; top: 140px; }
  .card--back { left: 630px; top: 388px; }

  .front-mark {
    position: absolute;
    inset: 0;
    display: flex;
    align-items: center;
    justify-content: center;
  }
  .brand-name {
    font-weight: 900;
    color: var(--ink);
    letter-spacing: 0.01em;
    text-transform: uppercase;
    line-height: 1;
  }
  .front-mark .brand-name { font-size: 30px; }

  .back-brand {
    position: absolute;
    right: 150px;
    top: 42px;
  }
  .back-brand .brand-name { font-size: 12px; }

  .wave { position: absolute; inset: 0; width: 500px; height: 286px; }

  .agent-photo {
    position: absolute;
    left: 338px;
    top: 56px;
    width: 124px;
    height: 124px;
    border-radius: 50%;
    border: 2px solid var(--ring);
    padding: 3px;
    background: var(--card);
  }
  .agent-photo span {
    display: block;
    width: 100%;
    height: 100%;
    border-radius: 50%;
    background: radial-gradient(circle at 50% 45%, var(--photo-warm), var(--photo-cool));
  }

  .agent {
    position: absolute;
    left: 34px;
    top: 126px;
  }
  .agent-name { font-size: 19px; font-weight: 700; color: var(--ink); line-height: 1.1; }
  .agent-title { font-size: 11px; font-weight: 700; color: var(--ink-soft); }

  .contacts {
    position: absolute;
    left: 34px;
    top: 194px;
    list-style: none;
    color: #fff;
    font-size: 11px;
    line-height: 1.3;
  }
  .contacts li { display: flex; align-items: flex-start; gap: 6px; margin-bottom: 1px; }
  .contacts li.address { margin-top: 5px; }
  .contacts svg { width: 11px; height: 11px; flex: none; margin-top: 2px; }
</style>
</head>
<body>

  <section class="card card--front" aria-label="Card front">
    <div class="front-mark">
      <span class="brand-name">Ridgeway Hearth Partners</span>
    </div>
  </section>

  <section class="card card--back" aria-label="Card back">
    <svg class="wave" viewBox="0 0 500 286" aria-hidden="true">
      <defs>
        <linearGradient id="waveFill" x1="0" y1="1" x2="1" y2="0">
          <stop offset="0" stop-color="var(--blue-deep)"/>
          <stop offset="1" stop-color="var(--blue-light)"/>
        </linearGradient>
      </defs>
      <path d="M0,182 C110,158 250,182 350,192 C430,200 470,150 500,96 L500,286 L0,286 Z" fill="url(#waveFill)"/>
    </svg>

    <div class="back-brand"><span class="brand-name">Ridgeway Hearth Partners</span></div>

    <div class="agent-photo" role="img" aria-label="Portrait photo of the agent"><span></span></div>

    <div class="agent">
      <p class="agent-name">Dana Merrill</p>
      <p class="agent-title">principal broker</p>
    </div>

    <ul class="contacts">
      <li>
        <svg viewBox="0 0 12 12" aria-hidden="true"><circle cx="6" cy="6" r="5.3" fill="none" stroke="#fff" stroke-width="1"/><path d="M4 3.5 L5 5 L4.6 5.6 Q5.4 6.8 6.4 7.4 L7 7 L8.5 8 L7.8 8.8 Q5 8.4 3.2 4.4 Z" fill="#fff"/></svg>
        <span>555.201.4830</span>
      </li>
      <li>
        <svg viewBox="0 0 12 12" aria-hidden="true"><circle cx="6" cy="6" r="5.3" fill="none" stroke="#fff" stroke-width="1"/><rect x="3.2" y="4" width="5.6" height="4.2" rx="0.8" fill="#fff"/></svg>
        <span>555.207.6614</span>
      </li>
      <li>
        <svg viewBox="0 0 12 12" aria-hidden="true"><circle cx="6" cy="6" r="5.3" fill="none" stroke="#fff" stroke-width="1"/><rect x="4.4" y="2.8" width="3.2" height="6.4" rx="0.6" fill="none" stroke="#fff" stroke-width="0.9"/></svg>
        <span>dana@ridgewayhearth.com</span>
      </li>
      <li>
        <svg viewBox="0 0 12 12" aria-hidden="true"><circle cx="6" cy="6" r="5.3" fill="none" stroke="#fff" stroke-width="1"/><rect x="3" y="3.6" width="6" height="4.2" fill="none" stroke="#fff" stroke-width="0.9"/><line x1="4.5" y1="9" x2="7.5" y2="9" stroke="#fff" stroke-width="0.9"/></svg>
        <span>ridgewayhearth-homes.com</span>
      </li>
      <li class="address">
        <svg viewBox="0 0 12 12" aria-hidden="true"><path d="M6 1 C3.6 1 2.2 2.8 2.2 4.6 C2.2 7.2 6 11 6 11 C6 11 9.8 7.2 9.8 4.6 C9.8 2.8 8.4 1 6 1 Z" fill="#fff"/><circle cx="6" cy="4.6" r="1.3" fill="var(--blue-deep)"/></svg>
        <span>482 Birch Ave Millbrook,<br>OR 97000</span>
      </li>
    </ul>
  </section>

</body>
</html>
```